2024 Comprehensive Needs Assessment

Design our 2024 Binder Report Cover. Front, Spine, Back. We are in the Education field, reporting data for strategic planning. I have attached our color palette and the previous years covers as a sample.

```html
<!DOCTYPE html>
<html lang="en">
<head>
<meta charset="utf-8">
<title>Alderbrook School District – Comprehensive Needs Assessment 2024</title>
<link rel="stylesheet" href="https://fonts.googleapis.com/css2?family=Bebas+Neue&family=Montserrat:wght@800;900&display=swap">
<style>
  :root {
    --teal: #00c7b8;
    --teal-veil: rgba(40, 205, 195, 0.62);
    --olive: #7f8a26;
    --blue: #4588b8;
    --red: #ff3347;
    --brown: #7a451b;
    --white: #ffffff;
    --shadow: rgba(20, 30, 40, 0.75);
  }
  * { margin: 0; padding: 0; box-sizing: border-box; }
  html, body { width: 809px; height: 1200px; overflow: hidden; }
  body { background: var(--teal); }
  .cover { position: relative; width: 809px; height: 1200px; background: var(--teal); }

  .hero-photo {
    position: absolute; left: 0; top: 0; width: 809px; height: 524px;
    background:
      radial-gradient(ellipse at 70% 35%, rgba(235,240,245,0.9) 0%, rgba(200,205,215,0.6) 35%, transparent 65%),
      linear-gradient(100deg, #e9c7b4 0%, #d9b6a4 25%, #9b9aa6 55%, #6b6f7a 75%, #5a4a3c 100%);
  }

  .title-band {
    position: absolute; left: 0; top: 100px; width: 809px; height: 196px;
    background: var(--teal-veil);
  }
  .title-band svg { display: block; width: 809px; height: 196px; }
  .district-name {
    font-family: 'Montserrat', sans-serif; font-weight: 900; fill: var(--white);
    filter: drop-shadow(3px 4px 2px var(--shadow));
  }

  .band {
    position: absolute; left: 0; width: 809px;
    display: flex; align-items: center; justify-content: center;
    font-family: 'Bebas Neue', sans-serif; color: var(--white);
    font-size: 106px; line-height: 1; padding-top: 8px;
  }
  .band--comprehensive { top: 525px; height: 142px; background: var(--olive); }
  .band--needs { top: 670px; height: 145px; background: var(--blue); }
  .band--assessment { top: 819px; height: 142px; background: var(--red); }

  .year-box {
    position: absolute; left: 166px; top: 1000px; width: 476px; height: 167px;
    background: var(--brown);
    display: flex; align-items: center; justify-content: center;
    font-family: 'Montserrat', sans-serif; font-weight: 900; color: var(--white);
    font-size: 128px; line-height: 1; letter-spacing: 2px;
  }
</style>
</head>
<body>
<main class="cover">
  <div class="hero-photo" role="img" aria-label="Photo of hands typing on a laptop showing a step diagram and colourful bar charts"></div>

  <header class="title-band">
    <svg viewBox="0 0 809 196" aria-label="Alderbrook School District">
      <text class="district-name" x="47" y="96" font-size="116" textLength="726" lengthAdjust="spacingAndGlyphs">ALDERBROOK</text>
      <text class="district-name" x="37" y="177" font-size="80" textLength="736" lengthAdjust="spacingAndGlyphs">SCHOOL DISTRICT</text>
    </svg>
  </header>

  <h1>
    <span class="band band--comprehensive">COMPREHENSIVE</span>
    <span class="band band--needs">NEEDS</span>
    <span class="band band--assessment">ASSESSMENT</span>
  </h1>

  <div class="year-box">2024</div>
</main>
</body>
</html>
```